We need a landing page for the company Vantrique. We are a startup and offer a device for use in the cosmetics and wellness industry. The application leads to skin improvements and more energy.

```html
<!DOCTYPE html>
<html lang="en">
<head>
<meta charset="UTF-8">
<title>Vantrique – cosmetics and wellness</title>
<link href="https://fonts.googleapis.com/css2?family=Roboto:wght@300;400;500;700&family=Open+Sans:ital,wght@0,400;0,600;1,400&display=swap" rel="stylesheet">
<style>
:root{
  --magenta:#c4168f;
  --magenta-dark:#a3127a;
  --pink-soft:#fbe9f7;
  --plum:#4a1738;
  --plum-dark:#2e0c22;
  --ink:#222;
  --text:#555;
  --line:#e3e3e3;
  --footer:#111;
  --white:#fff;
}
*{margin:0;padding:0;box-sizing:border-box}
html,body{width:1200px;height:4852px;overflow:hidden}
body{font-family:'Open Sans',sans-serif;color:var(--text);background:var(--white);position:relative}
.abs{position:absolute}
h2{font-family:'Roboto',sans-serif;font-weight:400;color:var(--ink);font-size:42px;text-align:center}
.btn{display:inline-block;border-radius:20px;font-family:'Roboto',sans-serif;font-size:14px;text-align:center}
.btn-fill{background:var(--magenta);color:var(--white)}
.btn-line{border:2px solid #bbb;color:#444;background:var(--white)}
.photo{position:absolute}

/* header */
.header{top:0;left:0;width:1200px;height:133px}
.brand{left:90px;top:32px;display:flex;align-items:center;gap:12px}
.brand-dot{width:64px;height:64px;border-radius:50%;border:5px solid var(--magenta)}
.brand-name{font-family:'Roboto',sans-serif;font-size:38px;font-weight:500;color:#333}
.contact-bar{right:115px;top:30px;display:flex;align-items:center;gap:16px;font-size:16px;color:#333}
.contact-bar .btn{padding:7px 16px}
.nav{right:115px;top:78px;display:flex;gap:40px;font-family:'Roboto',sans-serif;font-size:17px;color:#333}
.nav .active{color:var(--magenta)}

/* hero */
.hero{top:133px;left:0;width:1200px;height:557px;background:linear-gradient(110deg,#e9e3e1,#cfc3c2 55%,#b9a7ad);overflow:hidden}
.hero-circle{left:560px;top:-60px;width:760px;height:760px;border-radius:50%;background:rgba(196,22,143,.78)}
.hero-title{right:110px;top:185px;text-align:right;color:var(--white);font-family:'Roboto',sans-serif}
.hero-title .t1{font-size:86px;font-weight:700;letter-spacing:2px;line-height:1}
.hero-title .t2{font-size:40px;font-weight:500}
.hero-dots{right:45px;top:215px;display:flex;flex-direction:column;gap:12px}
.hero-dots span{width:11px;height:11px;border-radius:50%;background:#333}

/* about */
.about-title{top:800px;left:0;width:1200px}
.about-text{top:862px;left:200px;width:800px;text-align:center;font-size:15.5px;line-height:30px}
.arrow{width:34px;height:34px;border-radius:50%;border:1px solid #ccc;display:flex;align-items:center;justify-content:center;background:var(--white)}
.card{top:1035px;width:308px;height:285px;border:1px solid var(--line);background:var(--white);text-align:center;padding-top:95px}
.card.raised{box-shadow:0 6px 18px rgba(0,0,0,.15)}
.card-icon{position:absolute;left:50%;top:-58px;width:110px;height:110px;margin-left:-55px;border-radius:50%;background:var(--white);display:flex;align-items:center;justify-content:center}
.card-icon::before{content:"";position:absolute;inset:0;border-radius:50%;border:6px solid transparent;border-left-color:var(--magenta);border-bottom-color:var(--magenta);transform:rotate(20deg)}
.card-icon svg{width:56px;height:56px}
.card h3{font-family:'Roboto',sans-serif;font-weight:400;font-size:22px;color:#333;margin-bottom:10px}
.card p{font-size:13px;line-height:21px;padding:0 40px}
.card .btn{margin-top:22px;padding:5px 22px;font-size:13px}

/* products */
.products{top:1418px;left:0;width:1200px;height:502px;background:var(--pink-soft)}
.products-accent{left:90px;top:1488px;width:240px;height:155px;background:var(--magenta)}
.products-photo{left:115px;top:1512px;width:430px;height:338px;background:linear-gradient(135deg,#cfcfd3,#8f9099 60%,#5a5c68);border:6px solid var(--white);box-shadow:0 4px 14px rgba(0,0,0,.2)}
.play{left:300px;top:1652px;width:60px;height:60px;border-radius:50%;background:rgba(0,0,0,.55);display:flex;align-items:center;justify-content:center}
.products-body{left:600px;top:1545px;width:490px}
.products-body h2{text-align:left;font-size:44px;margin-bottom:18px}
.products-body p{font-size:14px;line-height:23px;color:#444}
.products-body .btn{margin-top:22px;padding:7px 24px;border-radius:3px;font-size:16px}

/* anti-aging */
.aging-title{top:2018px;left:0;width:1200px}
.tile{top:2143px;width:235px;height:257px;overflow:hidden}
.tile .photo{left:0;top:0;width:235px;height:257px}
.tile .label{position:absolute;left:0;bottom:0;width:235px;height:42px;background:var(--magenta);color:var(--white);font-family:'Roboto',sans-serif;font-weight:500;font-size:14px;display:flex;align-items:center;justify-content:center}

/* testimonials */
.testimonials{top:2503px;left:0;width:1200px;height:527px;background:linear-gradient(90deg,var(--plum-dark),var(--plum) 50%,var(--plum-dark))}
.testimonials h2{position:absolute;top:85px;left:0;width:1200px;color:var(--white)}
.quote-ring{left:125px;top:2650px;width:280px;height:280px;border-radius:50%;background:var(--magenta)}
.quote-photo{left:150px;top:2660px;width:270px;height:270px;border-radius:50%;background:linear-gradient(160deg,#e5e5e5,#8a8a8a 60%,#333)}
.quote{left:440px;top:2720px;width:605px;color:var(--white);font-size:14.5px;line-height:28px}
.quote .who{margin-top:12px;font-style:italic}
.chev{top:2755px}

/* blog */
.blog-title{top:3145px;left:0;width:1200px}
.blog-main{left:95px;top:3263px;width:495px;height:442px;box-shadow:0 4px 16px rgba(0,0,0,.15);background:var(--white)}
.blog-main .photo{left:0;top:0;width:495px;height:300px;background:linear-gradient(135deg,#f0ece9,#cbbdb6 55%,#8f9aa6)}
.blog-main .body{position:absolute;left:20px;top:290px;width:440px;background:var(--white);padding:12px 4px}
.blog-main h4{font-family:'Roboto',sans-serif;font-weight:500;font-size:18px;color:#222;margin-bottom:6px}
.blog-main p{font-size:12.5px;line-height:19px}
.blog-main .more{color:var(--magenta);font-size:12px;margin-top:6px}
.blog-item{left:635px;width:470px;height:135px;border-bottom:1px solid var(--line)}
.blog-item .photo{left:0;top:0;width:185px;height:120px;background:linear-gradient(135deg,#f3ece8,#d4bfb5 60%,#9c8e8a)}
.blog-item .text{position:absolute;left:225px;top:8px;width:245px}
.blog-item h5{font-family:'Roboto',sans-serif;font-weight:500;font-size:17px;color:#222;margin-bottom:4px}
.blog-item p{font-size:14px;line-height:22px;color:#333}
.blog-item .meta{display:flex;gap:14px;margin-top:8px}

/* contact */
.contact{top:3875px;left:0;width:1200px;height:555px;background:linear-gradient(90deg,#dcdcdc,#ececec 55%,#f3f3f3)}
.contact-photo{left:700px;top:3880px;width:420px;height:550px;background:linear-gradient(180deg,#c9a27a,#e7d6c6 45%,#f4f0ec)}
.contact h2{position:absolute;left:100px;top:95px;font-size:46px;text-align:left}
.field{background:var(--white);border:1px solid #aaa;font-size:13px;color:#444;padding:6px 10px;position:absolute}
.submit{left:100px;top:4285px;width:120px;height:36px;line-height:36px;font-size:17px;border-radius:20px}

/* footer */
.footer{top:4430px;left:0;width:1200px;height:422px;background:var(--footer);color:var(--white)}
.foot-brand{left:95px;top:4575px;display:flex;align-items:center;gap:12px}
.foot-brand .brand-name{color:var(--white)}
.foot-col{top:4518px;font-size:13px}
.foot-col h6{font-family:'Roboto',sans-serif;font-weight:400;font-size:18px;letter-spacing:1px;margin-bottom:22px}
.foot-col ul{list-style:none}
.foot-col li{margin-bottom:8px;display:flex;align-items:flex-start;gap:12px;line-height:18px}
.quick li::before{content:"";width:5px;height:5px;border-radius:50%;background:var(--white);margin-top:7px}
.quick li{margin-bottom:4px;gap:10px}
.social li{align-items:center;font-size:15px;margin-bottom:10px}
.social .ring{width:24px;height:24px;border-radius:50%;border:1.5px solid var(--white)}
.copyright{left:0;top:4790px;width:1200px;text-align:center;font-size:13px}
</style>
</head>
<body>

<!-- header -->
<header class="abs header">
  <div class="abs brand"><span class="brand-dot"></span><span class="brand-name">Vantrique</span></div>
  <div class="abs contact-bar">
    <span><svg width="16" height="16" viewBox="0 0 24 24"><path fill="#c4168f" d="M6.6 10.8a15 15 0 006.6 6.6l2.2-2.2a1 1 0 011-.25 11.4 11.4 0 003.6.57 1 1 0 011 1V20a1 1 0 01-1 1A17 17 0 013 4a1 1 0 011-1h3.5a1 1 0 011 1c0 1.25.2 2.45.57 3.6a1 1 0 01-.25 1z"/></svg> (+44) 200 555 0148</span>
    <span class="btn btn-fill">Make an Appointment</span>
  </div>
  <nav class="abs nav"><span class="active">Home</span><span>About us</span><span>Services</span><span>Products</span><span>Blog</span><span>Contact</span></nav>
</header>

<!-- hero -->
<section class="abs hero" role="img" aria-label="Woman relaxing on a treatment bed while receiving a cosmetic device treatment">
  <div class="abs hero-circle"></div>
  <div class="abs hero-title"><div class="t1">VANTRIQUE</div><div class="t2">cosmetics and wellness</div></div>
  <div class="abs hero-dots"><span></span><span></span><span></span></div>
</section>

<!-- about -->
<h2 class="abs about-title">About us</h2>
<p class="abs about-text">It is a long established fact that a reader will be distracted by the readable content of a page when looking at its layout. The point of using Lorem Ipsum is that it has a more-or-less normal distribution of</p>

<div class="abs arrow" style="left:40px;top:1158px"><svg width="12" height="12" viewBox="0 0 12 12"><path d="M8 1L3 6l5 5" stroke="#666" stroke-width="1.5" fill="none"/></svg></div>
<div class="abs arrow" style="left:1098px;top:1158px"><svg width="12" height="12" viewBox="0 0 12 12"><path d="M4 1l5 5-5 5" stroke="#666" stroke-width="1.5" fill="none"/></svg></div>

<div class="abs card" style="left:107px">
  <div class="card-icon"><svg viewBox="0 0 56 56"><rect x="14" y="10" width="28" height="36" rx="3" fill="none" stroke="#333" stroke-width="2"/><circle cx="28" cy="24" r="6" fill="none" stroke="#333" stroke-width="2"/><path d="M19 40c2-6 16-6 18 0" fill="none" stroke="#333" stroke-width="2"/></svg></div>
  <h3>Improved Sleep</h3>
  <p>It is a long established fact that a reader will be distracted by the readable content of a page</p>
  <span class="btn btn-line">Read More</span>
</div>
<div class="abs card raised" style="left:433px">
  <div class="card-icon"><svg viewBox="0 0 56 56"><rect x="12" y="12" width="32" height="32" rx="4" fill="none" stroke="#333" stroke-width="2"/><circle cx="28" cy="28" r="10" fill="none" stroke="#333" stroke-width="2"/><path d="M16 16l24 24" stroke="#333" stroke-width="2"/></svg></div>
  <h3>No more cravings</h3>
  <p>It is a long established fact that a reader will be distracted by the readable content of a page</p>
  <span class="btn btn-fill">Read More</span>
</div>
<div class="abs card" style="left:760px">
  <div class="card-icon"><svg viewBox="0 0 56 56"><path d="M18 10c2 10 2 16-2 24 3 6 4 9 4 14M38 10c-2 10-2 16 2 24-3 6-4 9-4 14" fill="none" stroke="#333" stroke-width="2"/><path d="M22 30h12" stroke="#333" stroke-width="2"/></svg></div>
  <h3>Better Metabolism</h3>
  <p>It is a long established fact that a reader will be distracted by the readable content of a page</p>
  <span class="btn btn-line">Read More</span>
</div>

<!-- products -->
<section class="abs products"></section>
<div class="abs products-accent"></div>
<div class="abs products-photo" role="img" aria-label="Practitioner operating a wellness device beside a seated client in a clinic"></div>
<div class="abs play"><svg width="22" height="22" viewBox="0 0 22 22"><path d="M6 3l13 8-13 8z" fill="#fff"/></svg></div>
<div class="abs products-body">
  <h2>Products &amp; Services</h2>
  <p>It is a long established fact that a reader will be distracted by the readable content of a page when looking at its layout. The point of using Lorem Ipsum is that it has a more-or-less normal distribution of letters, as opposed to using 'Content here, content here', making it look like readable English. Many desktop publishing packages and web page editors now use Lorem Ipsum as their default model text, and a search</p>
  <span class="btn btn-fill">Read More</span>
</div>

<!-- anti-aging -->
<h2 class="abs aging-title">The new anti-aging wonder</h2>
<div class="abs tile" style="left:95px"><div class="photo" role="img" aria-label="Slim waist being measured with a tape" style="background:linear-gradient(135deg,#f1e3d6,#d8b59b 60%,#a9826b)"></div><div class="label">Vantrique Is A Non-invasive</div></div>
<div class="abs tile" style="left:345px"><div class="photo" role="img" aria-label="Client receiving a facial revitalization treatment" style="background:linear-gradient(135deg,#f4ebe4,#d9c2b3 60%,#8fa3b3)"></div><div class="label">Effective Revitalization</div></div>
<div class="abs tile" style="left:600px"><div class="photo" role="img" aria-label="Aesthetician treating a client's face with a handheld device" style="background:linear-gradient(135deg,#eee4e0,#c9a9a2 55%,#7d6f79)"></div><div class="label">Pain-free High-tech Aesthetic</div></div>
<div class="abs tile" style="left:852px"><div class="photo" role="img" aria-label="Specialist applying a light-based device in a treatment room" style="background:linear-gradient(135deg,#e6e7ee,#a8adc3 55%,#5d627e)"></div><div class="label">Spontaneous Electromagnetic</div></div>

<!-- testimonials -->
<section class="abs testimonials" role="img" aria-label="Dark plum background with a faint treatment scene"><h2>Testimonials</h2></section>
<div class="abs quote-ring"></div>
<div class="abs quote-photo" role="img" aria-label="Black and white portrait of a smiling client"></div>
<div class="abs quote">
  <p>" It is a long established fact that a reader will be distracted by the readable content of a page when looking at its layout. The point of using Lorem Ipsum is that it has a more-or-less normal distribution of letters, as opposed to using 'Content here, content here', making it look like readable English. Many desktop publishing packages and web page editors now use Lorem Ipsum as their default model text "</p>
  <p class="who">- MARLO, CLIENT AT LUMEN SKIN STUDIO</p>
</div>
<svg class="abs chev" style="left:50px" width="40" height="70" viewBox="0 0 40 70"><path d="M34 4L6 35l28 31" stroke="#fff" stroke-width="3" fill="none"/></svg>
<svg class="abs chev" style="left:1090px" width="40" height="70" viewBox="0 0 40 70"><path d="M6 4l28 31L6 66" stroke="#fff" stroke-width="3" fill="none"/></svg>

<!-- blog -->
<h2 class="abs blog-title">Latest Blog</h2>
<article class="abs blog-main">
  <div class="photo" role="img" aria-label="Beautician using a device on a client's face"></div>
  <div class="body">
    <h4>Neque porro quisquam est qui dolorem</h4>
    <p>It is a long established fact that a reader will be distracted by the readable content of a page when looking at its layout. The point of using Lorem Ipsum is that it has a more-or-less normal distribution</p>
    <div class="more">Read More »</div>
  </div>
</article>

<article class="abs blog-item" style="top:3263px">
  <div class="photo" role="img" aria-label="Woman with a facial treatment mask"></div>
  <div class="text"><h5>Neque porro quisquam est</h5><p>Ipsum is simply dummy text of the printing and type page when</p>
    <div class="meta"><svg width="16" height="16" viewBox="0 0 16 16"><path d="M8 1l2 5h5l-4 3 1.5 5L8 11l-4.5 3L5 9 1 6h5z" fill="none" stroke="#888"/></svg><svg width="16" height="16" viewBox="0 0 16 16"><rect x="1.5" y="3" width="13" height="10" fill="none" stroke="#888"/><path d="M1.5 3L8 9l6.5-6" fill="none" stroke="#888"/></svg><svg width="16" height="16" viewBox="0 0 16 16"><circle cx="8" cy="5" r="3" fill="none" stroke="#888"/><path d="M2 15c0-4 12-4 12 0" fill="none" stroke="#888"/></svg></div></div>
</article>
<article class="abs blog-item" style="top:3418px">
  <div class="photo" role="img" aria-label="Woman with a towel wrap smiling after a facial"></div>
  <div class="text"><h5>Porro quisquam est dolorem</h5><p>Ipsum is simply dummy text of the printing and type page when</p>
    <div class="meta"><svg width="16" height="16" viewBox="0 0 16 16"><path d="M8 1l2 5h5l-4 3 1.5 5L8 11l-4.5 3L5 9 1 6h5z" fill="none" stroke="#888"/></svg><svg width="16" height="16" viewBox="0 0 16 16"><rect x="1.5" y="3" width="13" height="10" fill="none" stroke="#888"/><path d="M1.5 3L8 9l6.5-6" fill="none" stroke="#888"/></svg><svg width="16" height="16" viewBox="0 0 16 16"><circle cx="8" cy="5" r="3" fill="none" stroke="#888"/><path d="M2 15c0-4 12-4 12 0" fill="none" stroke="#888"/></svg></div></div>
</article>
<article class="abs blog-item" style="top:3573px;border-bottom:none">
  <div class="photo" role="img" aria-label="Client lying down during a facial device session"></div>
  <div class="text"><h5>Dolorem ipsum quia dolor</h5><p>Ipsum is simply dummy text of the printing and type page when</p>
    <div class="meta"><svg width="16" height="16" viewBox="0 0 16 16"><path d="M8 1l2 5h5l-4 3 1.5 5L8 11l-4.5 3L5 9 1 6h5z" fill="none" stroke="#888"/></svg><svg width="16" height="16" viewBox="0 0 16 16"><rect x="1.5" y="3" width="13" height="10" fill="none" stroke="#888"/><path d="M1.5 3L8 9l6.5-6" fill="none" stroke="#888"/></svg><svg width="16" height="16" viewBox="0 0 16 16"><circle cx="8" cy="5" r="3" fill="none" stroke="#888"/><path d="M2 15c0-4 12-4 12 0" fill="none" stroke="#888"/></svg></div></div>
</article>

<!-- contact -->
<section class="abs contact"><h2>Contact us</h2></section>
<div class="abs contact-photo" role="img" aria-label="Smiling woman with long wavy hair in a white top"></div>
<div class="field" style="left:100px;top:4060px;width:240px;height:44px">Name</div>
<div class="field" style="left:358px;top:4060px;width:240px;height:44px">Phone</div>
<div class="field" style="left:100px;top:4118px;width:240px;height:44px">Email</div>
<div class="field" style="left:358px;top:4118px;width:240px;height:44px">Address</div>
<div class="field" style="left:100px;top:4176px;width:498px;height:88px">Message</div>
<span class="abs btn btn-fill submit">Submit</span>

<!-- footer -->
<footer class="abs footer"></footer>
<div class="abs foot-brand"><span class="brand-dot"></span><span class="brand-name">Vantrique</span></div>
<div class="abs foot-col" style="left:440px;color:#fff">
  <h6>CONTACT US</h6>
  <ul>
    <li><svg width="14" height="18" viewBox="0 0 14 18"><path d="M7 0a7 7 0 017 7c0 5-7 11-7 11S0 12 0 7a7 7 0 017-7z" fill="#fff"/><circle cx="7" cy="7" r="2.5" fill="#111"/></svg><span>42 Harbour Lane<br>Brightwell VIC 3999</span></li>
    <li><svg width="14" height="14" viewBox="0 0 24 24"><path fill="#fff" d="M6.6 10.8a15 15 0 006.6 6.6l2.2-2.2a1 1 0 011-.25 11.4 11.4 0 003.6.57 1 1 0 011 1V20a1 1 0 01-1 1A17 17 0 013 4a1 1 0 011-1h3.5a1 1 0 011 1c0 1.25.2 2.45.57 3.6a1 1 0 01-.25 1z"/></svg><span>(03) 5550 1729</span></li>
    <li><svg width="14" height="12" viewBox="0 0 14 12"><rect width="14" height="12" fill="#fff"/><path d="M0 0l7 6 7-6" stroke="#111" fill="none"/></svg><span>hello@vantrique-mail.com</span></li>
  </ul>
</div>
<div class="abs foot-col quick" style="left:715px;color:#fff">
  <h6>QUICK LINKS</h6>
  <ul><li>Home</li><li>About us</li><li>Product</li><li>Services</li><li>Contact Us</li></ul>
</div>
<div class="abs foot-col social" style="left:935px;color:#fff">
  <h6>FOLLOW US</h6>
  <ul><li><span class="ring"></span>Linkora</li><li><span class="ring"></span>Chirper</li><li><span class="ring"></span>Circlehub</li><li><span class="ring"></span>Vidstream</li></ul>
</div>
<p class="abs copyright" style="color:#fff">© Copyright 2019 . All Rights Reserved. Terms and Conditions | Privacy Policy</p>

</body>
</html>
```